依頼詳細
買取対象はCD,DVD,本、ゲームソフト、ゲーム機本体です。デザインはファイル形式で送って頂き、
僕が受け取った後、すぐにでも看板制作会社及びビラ制作会社に依頼できるようにしてください。店舗の
写真を念のため添付しますので、イメージ作りに役立てて下さい。社名はホシノトレード ですので、
リサイクルの三角形のおなじみのマークは必ず看板及びチラシのデザインに含めて下さい。
記載項目
会社名、電話、メアド、ロゴ、コメント書き込み欄
希望イメージ
シンプル 複雑
単色 カラフル
暗い 明るい
日常 高級
遊び心 厳粛
未来的 伝統的
女性的 男性的
希望する色
納品ファイル
• 高解像度JPG (.jpg)
補足説明
金額を増やしました。よろしくお願いします。依頼内容について不明な点がありましたらなんなりとご質問下さい。
.
写真を添付しました。
店の名前は ホシノトレードです。 人通りの多い商店街に近い交差点の信号待ちの場所に近いところにオープンしますので、目につきやすい看板を希望しております。店の電話番号は決まっていますので、お仕事発注後にお伝えします。できれば発注後にメールで何回かのやり取りをさせて頂きたいと思っており、その点ご了承頂ける方に受注頂きたいと考えております。よろしくお願い致します。
選択させて頂いた提案物の著作権(財産権)等の扱いはTaskmill利用規約に従い、弊社に譲渡をお願いします。フォントや画像素材などを利用する場合は上記利用用途に使用できることを確認し、第三者の知的財産権等に注意してください

シンプルで気に入りました。

皆様ありがとうございました。またよろしくお願いします。

```html
<!DOCTYPE html>
<html lang="ja">
<head>
<meta charset="UTF-8">
<title>ホシノトレード 中古品買取</title>
<link rel="stylesheet" href="https://fonts.googleapis.com/css2?family=M+PLUS+Rounded+1c:wght@500;700;800&display=swap">
<style>
  :root {
    --lime: #8dc21f;
    --lime-light: #b4d94c;
    --lime-dark: #6fa313;
    --pink: #e4007f;
    --red: #e60012;
    --orange: #f6a200;
    --ink: #222222;
    --white: #ffffff;
    --cream: #fbfbef;
    --grey: #9a9a9a;
    --book-tone: #c9b58a;
    --disc-tone: #c8b98a;
    --console-tone: #dcdcdc;
  }
  * { margin: 0; padding: 0; box-sizing: border-box; }
  html, body { width: 849px; height: 1200px; overflow: hidden; }
  body {
    position: relative;
    background: var(--lime);
    font-family: "M PLUS Rounded 1c", sans-serif;
    color: var(--ink);
  }
  .header {
    position: absolute; left: 0; top: 0; width: 849px; height: 283px;
    background: var(--lime-light);
  }
  .title {
    position: absolute; left: 100px; top: 125px; width: 650px; height: 147px;
    background: var(--white);
    border-radius: 14px;
    border: 6px solid var(--lime-dark);
    display: flex; align-items: center; justify-content: center;
    font-size: 112px; font-weight: 800; color: var(--pink);
    letter-spacing: 8px;
  }
  .items {
    position: absolute; left: 14px; top: 283px; width: 821px; height: 652px;
    background: linear-gradient(var(--white), var(--cream));
  }
  .line {
    position: absolute; font-weight: 700; font-size: 62px; line-height: 1; white-space: nowrap;
  }
  .line-media { left: 100px; top: 40px; letter-spacing: 10px; }
  .line-soft { right: 80px; top: 112px; }
  .line-console { left: 135px; top: 188px; }
  .line-console small { font-size: 36px; margin-left: 10px; }
  .headline {
    position: absolute; left: 0; width: 100%; top: 262px; text-align: center;
    font-size: 98px; font-weight: 800; color: var(--red); line-height: 1;
  }
  .art { position: absolute; border-radius: 10px; }
  .art-books { left: 36px; top: 417px; width: 220px; height: 220px; background: linear-gradient(135deg, #d9c8a0, var(--book-tone)); }
  .art-disc { left: 296px; top: 437px; width: 180px; height: 180px; border-radius: 50%; background: radial-gradient(circle, #f2ecd6, var(--disc-tone)); }
  .art-console { left: 506px; top: 392px; width: 270px; height: 250px; background: linear-gradient(135deg, #f0f0f0, var(--console-tone)); }
  .shop {
    position: absolute; left: 30px; top: 955px; color: var(--white);
  }
  .shop-name { font-size: 46px; font-weight: 800; color: var(--orange); line-height: 1.1; }
  .shop-phone { font-size: 40px; font-weight: 700; margin-top: 14px; line-height: 1; }
  .shop-detail { font-size: 22px; font-weight: 700; margin-top: 10px; line-height: 1.3; }
  .comment-box {
    position: absolute; left: 453px; top: 977px; width: 311px; height: 183px;
    background: var(--white); border-radius: 12px;
    display: flex; align-items: center; justify-content: center;
    color: var(--grey); font-size: 20px;
  }
  .recycle-mark {
    position: absolute; left: 722px; top: 1090px; width: 100px; height: 100px;
    border-radius: 50%; background: var(--white);
    display: flex; align-items: center; justify-content: center;
  }
</style>
</head>
<body>
  <header class="header">
    <h1 class="title">中古品買取</h1>
  </header>

  <section class="items">
    <p class="line line-media">CD DVD 本</p>
    <p class="line line-soft">ゲームソフト</p>
    <p class="line line-console">ゲーム機本体<small>など</small></p>
    <p class="headline">高価買い取り中!</p>
    <div class="art art-books" role="img" aria-label="積み重ねた本のイラスト"></div>
    <div class="art art-disc" role="img" aria-label="CD・DVDディスクのイラスト"></div>
    <div class="art art-console" role="img" aria-label="携帯ゲーム機本体のイラスト"></div>
  </section>

  <footer class="shop">
    <p class="shop-name">ホシノトレード</p>
    <p class="shop-phone">
      <svg width="34" height="30" viewBox="0 0 34 30" aria-hidden="true"><path d="M3 10 Q17 0 31 10 L27 14 L22 11 L22 8 Q17 6 12 8 L12 11 L7 14 Z M8 16 H26 L30 28 H4 Z" fill="#ffffff"/></svg>00-0000-0000
    </p>
    <p class="shop-detail">所在地：〒000-0000<br>○○○○○○○○○○○○<br>E-mail:○○○○○@○○○○ne.jp</p>
  </footer>

  <div class="comment-box">コメント欄</div>
  <div class="recycle-mark" role="img" aria-label="リサイクルマーク">
    <svg width="70" height="70" viewBox="0 0 70 70" aria-hidden="true"><circle cx="35" cy="35" r="30" fill="#6fa313"/></svg>
  </div>
</body>
</html>
```